Real Estate Savvy Investors looking to expand and fuel homeownership possibilities.

My company is called Tavmoor Holdings, LLC. My team specializes in residential and commercial real estate. We buy, sell and rent, FAST! We buy houses in any situation and condition, including Pre-Foreclosures and vacant homes. We trade homes and We provide creative financing, such as our lease to own option, in which we accept goods such as cars, boats etc., to go towards the purchase price of the home. In commercial real estate, we buy in any area and we are open to creative financing.

Target Market(s)

Preforeclosure homes, vacant homes, distressed homes, all home owners

Industry/Entity Type

Real Estate

Contact Information for Business Card

Should include company name (Tavmoor Holdings, LLC), company email TavmoorHoldingsLLC@quenmail.com, office phone 405-738-2914, P.O. Box 58037, ok, ok 73982)

Font styles to use
Serif

Colors

Designer to choose colors to be used in the design.

Requirements
Must have
• Must include what we specialize in: preforeclosures, vacant homes, distressed homes-any situation and condition.
• Somewhere on the card please include: Investment opportunities: 8%-10% return.

```html
<!DOCTYPE html>
<html lang="en">
<head>
<meta charset="utf-8">
<title>Tavmoor Holdings, LLC – Business Card</title>
<link href="https://fonts.googleapis.com/css2?family=Open+Sans:wght@400;600;700&display=swap" rel="stylesheet">
<style>
  :root {
    --stage: #e9e6e1;
    --card-dark: #2b2b2d;
    --card-light: #ffffff;
    --ink: #222226;
    --steel: #8d8f94;
    --blue: #2f6bc0;
    --muted: #55575c;
  }
  * { box-sizing: border-box; margin: 0; padding: 0; }
  html, body { width: 1200px; height: 800px; overflow: hidden; }
  body {
    background: var(--stage);
    font-family: "Open Sans", Arial, sans-serif;
    display: flex; align-items: center; justify-content: center; gap: 50px;
  }
  .card {
    position: relative; width: 525px; height: 300px;
    border-radius: 18px; overflow: hidden;
    box-shadow: 0 10px 26px rgba(0,0,0,.18);
  }
  /* Front */
  .card-front { background: var(--card-dark); color: var(--steel); }
  .front-tagline {
    position: absolute; top: 22px; right: 28px;
    color: var(--blue); font-size: 13px; font-weight: 600;
  }
  .front-brand {
    position: absolute; left: 60px; top: 92px;
    display: flex; align-items: center; gap: 12px;
  }
  .brand-square { width: 16px; height: 16px; background: var(--blue); }
  .front-brand .brand-name { font-size: 33px; font-weight: 600; color: var(--steel); letter-spacing: .3px; }
  .front-service {
    position: absolute; left: 88px; top: 142px;
    font-size: 14px; font-weight: 600; color: var(--blue);
  }
  .front-specialties {
    position: absolute; left: 88px; top: 166px;
    font-size: 13px; color: var(--steel);
  }
  .front-invest {
    position: absolute; left: 28px; bottom: 24px;
    font-size: 14px; font-weight: 600; color: var(--blue);
  }
  /* Back */
  .card-back { background: var(--card-light); color: var(--ink); }
  .back-brand {
    position: absolute; right: 30px; top: 30px;
    display: flex; align-items: center; gap: 10px;
  }
  .back-brand .brand-square { width: 12px; height: 12px; }
  .back-brand .brand-name { font-size: 19px; font-weight: 400; color: var(--ink); }
  .person {
    position: absolute; left: 0; top: 150px;
    padding-left: 30px; border-left: 9px solid var(--blue);
  }
  .person-name { font-size: 24px; font-weight: 700; line-height: 1.1; }
  .person-title { font-size: 15px; color: var(--blue); }
  .contact-list {
    position: absolute; left: 30px; bottom: 26px;
    list-style: none; font-size: 13px; color: var(--muted);
  }
  .contact-list li { display: flex; align-items: center; gap: 12px; height: 24px; }
  .contact-list svg { width: 15px; height: 15px; fill: var(--blue); flex: none; }
  .contact-rule {
    position: absolute; left: 340px; right: 0; bottom: 78px;
    height: 3px; background: var(--blue);
  }
</style>
</head>
<body>
  <section class="card card-front" aria-label="Card front">
    <p class="front-tagline">Buy, Sell, Rent, Lease To Own.</p>
    <div class="front-brand">
      <span class="brand-square"></span>
      <span class="brand-name">Tavmoor Holdings, LLC</span>
    </div>
    <p class="front-service">Residential and Commercial Real Estate</p>
    <p class="front-specialties">Pre-Foreclosures | Vacant Homes | Distressed Homes</p>
    <p class="front-invest">Investment Opportunities: 8%-10% Return.</p>
  </section>

  <section class="card card-back" aria-label="Card back">
    <div class="back-brand">
      <span class="brand-square"></span>
      <span class="brand-name">Tavmoor Holdings, LLC</span>
    </div>
    <div class="person">
      <p class="person-name">Your Name</p>
      <p class="person-title">Job Title</p>
    </div>
    <div class="contact-rule"></div>
    <ul class="contact-list">
      <li>
        <svg viewBox="0 0 16 16" aria-hidden="true"><path d="M1 3h14v10H1z M1 3l7 6 7-6" /></svg>
        TavmoorHoldingsLLC@quenmail.com
      </li>
      <li>
        <svg viewBox="0 0 16 16" aria-hidden="true"><path d="M3 1h4l1 4-2 1.5c1 2 2.5 3.5 4.5 4.5L12 9l4 1v4c0 1-1 2-2 2C7 16 0 9 0 3c0-1 1-2 2-2z"/></svg>
        405-738-2914
      </li>
      <li>
        <svg viewBox="0 0 16 16" aria-hidden="true"><path d="M8 0a5.5 5.5 0 0 0-5.5 5.5C2.5 10 8 16 8 16s5.5-6 5.5-10.5A5.5 5.5 0 0 0 8 0zm0 8a2.5 2.5 0 1 1 0-5 2.5 2.5 0 0 1 0 5z"/></svg>
        P.O. Box 58037, OKC 73982
      </li>
    </ul>
  </section>
</body>
</html>
```